New letterhead/ stationary design for insurance restoration builder

Modern, clever creative not cheap tacky design maroon and black / white are logo colours. Company name is Harbor Peak Building Services. Might need two different versions of new design, one for standard letterhead communicatio, the other i need to use for management aystems policies amd procedirrs etc.becauuse you wong have tome
Target Market(s)
Large residential insurance companies and their clients, tradespeople and the integrated management system with policies and procedures is internal company employees.
Font styles to use
Requirements
Must have
- A version that would be used as a typical business letterhead is and the other needs to be in a format / design that suits company policies and procedures. Be professional, HARBOR PEAK and be creative / totally custom for pur business not just an edited version of what you can get for free in Word or off the internet pls. Incorporating industry relevant shapes or placement to create the illusion of a residential construction related image is an idea. Someone who is cleverly creative with simple but impactdul design will get my interest.
Nice to have
- Can have different shades of the corporate colours used which are maroon / burgundy and black. https://fernlowmedia.example/common/images/v3/sketch-icon-dropzone.png
Should not have
- Look like the genetic templates and designs you can do yourself copying off the internet.

```html
<!DOCTYPE html>
<html lang="en">
<head>
<meta charset="utf-8">
<title>Harbor Peak Building Services — Letterhead</title>
<link href="https://fonts.googleapis.com/css2?family=Lato:wght@300;400;700;900&family=Pinyon+Script&display=swap" rel="stylesheet">
<style>
  :root {
    --maroon: #981b45;
    --maroon-deep: #8e1a33;
    --ink: #2e2e2e;
    --ink-soft: #4a4a4a;
    --paper: #f3f3f3;
    --backdrop: #e4e4e4;
  }
  * { box-sizing: border-box; margin: 0; padding: 0; }
  html, body {
    width: 1200px; height: 1200px; overflow: hidden;
    background: var(--backdrop);
    font-family: "Lato", sans-serif;
  }
  .letterhead {
    position: absolute; left: 200px; top: 34px;
    width: 800px; height: 1131px;
    background: var(--paper);
    color: var(--ink-soft);
  }
  .brand {
    position: absolute; left: 67px; top: 34px;
    width: 190px;
    display: flex; align-items: flex-start; gap: 10px;
  }
  .brand-square {
    flex: none; width: 18px; height: 18px; margin-top: 6px;
    background: var(--maroon);
  }
  .brand-name {
    font-weight: 900; color: var(--maroon);
    font-size: 30px; line-height: 32px; letter-spacing: -0.3px;
  }
  .contact {
    position: absolute; left: 320px; top: 94px;
    width: 178px;
    font-size: 12.6px; line-height: 16.2px; color: var(--ink);
    list-style: none; white-space: nowrap;
  }
  .contact li { display: flex; align-items: center; gap: 7px; }
  .contact svg { width: 10px; height: 10px; fill: var(--maroon); flex: none; }
  .divider {
    position: absolute; left: 512px; top: 105px;
    width: 1.5px; height: 48px; background: var(--maroon);
  }
  .address {
    position: absolute; left: 528px; top: 110px;
    font-size: 12.6px; line-height: 16.2px; color: var(--ink);
    font-style: normal; white-space: nowrap;
  }
  .letter {
    position: absolute; left: 85px; top: 249px; width: 630px;
    font-size: 12.6px; line-height: 18.9px; font-weight: 300;
  }
  .date { margin-bottom: 19px; }
  .recipient { margin-bottom: 37px; }
  .recipient strong { font-weight: 700; color: #111; }
  .salutation { margin-bottom: 19px; }
  .letter p.body { text-align: justify; margin-bottom: 18.9px; }
  .closing { margin-top: 56px; }
  .signature {
    font-family: "Pinyon Script", cursive;
    font-size: 25px; line-height: 30px; color: #111; margin-top: 6px;
  }
  .footer-band {
    position: absolute; left: 0; top: 1083px; width: 800px; height: 36px;
    background: var(--maroon-deep); color: #fff;
    display: flex; align-items: center; justify-content: center;
    font-size: 12.6px; font-weight: 400;
  }
  .footer-band strong { font-weight: 700; margin-right: 4px; }
</style>
</head>
<body>
<main class="letterhead">
  <header>
    <div class="brand">
      <span class="brand-square"></span>
      <span class="brand-name">Harbor Peak Building Services</span>
    </div>
    <ul class="contact">
      <li><svg viewBox="0 0 10 10"><path d="M2 0.5 L3.8 2.6 L2.8 3.6 Q4 6 6.4 7.2 L7.4 6.2 L9.5 8 L8.2 9.5 Q3 9 0.5 1.8 Z"/></svg>03 5550 1820</li>
      <li><svg viewBox="0 0 10 10"><rect x="2.5" y="0.5" width="5" height="2.5"/><rect x="0.5" y="3.5" width="9" height="4"/><rect x="2.5" y="6.5" width="5" height="3"/></svg>03 5550 1821</li>
      <li><svg viewBox="0 0 10 10"><path d="M0.5 2 H9.5 V8 H0.5 Z M0.5 2 L5 5.5 L9.5 2" fill="none" stroke="#981b45" stroke-width="1.4"/></svg>info@harborpeak.example</li>
      <li><svg viewBox="0 0 10 10"><circle cx="5" cy="5" r="4.3" fill="none" stroke="#981b45" stroke-width="1.1"/><ellipse cx="5" cy="5" rx="1.8" ry="4.3" fill="none" stroke="#981b45" stroke-width="0.9"/><path d="M0.7 5 H9.3" stroke="#981b45" stroke-width="0.9"/></svg>www.harborpeak.example</li>
    </ul>
    <span class="divider"></span>
    <address class="address">
      Harbor Peak Building Services Pty Ltd<br>
      48 Tallow Crescent<br>
      Brambleton Victoria 3999
    </address>
  </header>

  <section class="letter">
    <p class="date">01 January 2050</p>
    <p class="recipient"><strong>Company (Pvt) Ltd.</strong><br>PO Box 3355 Mainville St<br>Sample City Country 3355</p>
    <p class="salutation">Dear Martin Ellsworth,</p>
    <p class="body">Lorem ipsum dolor sit amet, consectetuer adipiscing elit, sed diam nonummy nibh euismod tincidunt ut laoreet dolore magna aliquam erat volutpat. Ut wisi enim ad minim veniam, quis nostrud exerci tation ullamcorper suscipit lobortis nisl ut aliquip ex ea commodo consequat. Duis dolore te feugait nulla facilisi. Nam liber tempor cum soluta nobis eleifend option congue nihil imperdiet doming id quod mazim placerat facer possim assum. Lorem ipsum dolor sit amet, consectetuer adipiscing elit, sed diam nonummy nibh euismod tincidunt ut laoreet dolore magna aliquam erat volutpat. Ut wisi enim ad minim veniam, quis nostrud exerci tation ullamcorper suscipit lobortis nisl ut aliquip ex ea commodo consequat.</p>
    <p class="body">Consectetuer adipiscing elit, sed diam nonummy nibh euismod tincidunt ut laoreet dolore magna aliquam erat volutpat. Ut wisi enim ad minim veniam, quis nostrud exerci tation ullamcorper suscipit lobortis nisl ut aliquip ex ea commodo consequat. Consectetuer adipiscing elit, sed diam nonummy nibh euismod tincidunt ut laoreet dolore magna aliquam erat volutpat. Ut wisi enim ad minim veniam, quis nostrud exerci tation ullamcorper suscipit lobortis nisl ut aliquip ex ea commodo consequat.</p>
    <p class="body">Consectetuer adipiscing elit, sed diam nonummy nibh euismod tincidunt ut laoreet dolore magna aliquam erat volutpat. Ut wisi enim ad minim veniam, quis nostrud exerci tation ullamcorper suscipit lobortis nisl ut aliquip ex ea commodo consequat. Consectetuer adipiscing elit, sed diam nonummy nibh euismod tincidunt ut laoreet dolore magna aliquam erat volutpat. Ut wisi enim ad minim veniam, quis nostrud exerci tation ullamcorper suscipit lobortis nisl ut aliquip ex ea commodo consequat.</p>
    <p class="closing">Sincerely Yours</p>
    <p class="signature">Gregory Alan Whitcombe</p>
  </section>

  <footer class="footer-band">
    <strong>Harbor Peak Building Services</strong> specialises in home maintenance, renovations, and insurance assessed building repairs.
  </footer>
</main>
</body>
</html>
```